Robotic startup business cards

We are looking for a design for a set of business cards which reflect the spirit and humor of Torvexa Robotics. We want to present ourselves as sleek, professional, but laid-back consulting company.

We primarily focus on developing robotic arms software. This software controls robots and does things like grab items, pick objects up, move them, etc.

We want to allow you maximum design creativity, but do ask that you consider our existing style guidelines (see attached files) in order to make our brand cohesive.

Target Market(s)

Startups and Mid-size robotic companies

Industry/Entity Type

Business

Contact Information for Business Card

Liam Brantly, PhD
Roboticist | Torvexa Consulting | 318.572.6094

Font styles to use
Other font styles liked:
• Source code pro

Requirements
Must have
• robots or robotic arms
• similar color scheme that works with existing brand guidelines
Nice to have
• please consider our existing style guidelines (see attached files) in order to make our brand cohesive.
• minimalism style is generally nice.
Should not have
• An old, boring, or corporate feel. Too much text.

```html
<!DOCTYPE html>
<html lang="en">
<head>
<meta charset="utf-8">
<title>Torvexa Robotics – Business Cards</title>
<link rel="stylesheet" href="https://fonts.googleapis.com/css2?family=Lato:wght@400;700;900&family=Source+Code+Pro:wght@300;400&display=swap">
<style>
  :root {
    --backdrop: #3b3532;
    --card: #0b0b0b;
    --card-edge: #1a1a1a;
    --mint: #10e3a0;
    --ink-light: #e9e9e9;
    --silver: #c9c9c9;
    --divider: #2e2e2e;
  }
  * { margin: 0; padding: 0; box-sizing: border-box; }
  html, body {
    width: 1200px; height: 900px; overflow: hidden;
    background: var(--backdrop);
  }
  .sheet {
    position: relative; width: 1200px; height: 900px;
  }
  .card {
    position: absolute; top: 300px;
    width: 520px; height: 300px;
    background: var(--card);
    border: 1px solid var(--card-edge);
    box-shadow: 0 10px 30px rgba(0,0,0,0.45);
  }
  .card--contact { left: 50px; }
  .card--brand { left: 630px; }

  /* contact side */
  .brand-mark {
    position: absolute; left: 46px; top: 0; height: 100%;
    display: flex; align-items: center;
    font-family: "Lato", sans-serif; font-weight: 900;
    font-size: 34px; color: var(--mint); letter-spacing: 0.5px;
  }
  .divider {
    position: absolute; left: 232px; top: 70px;
    width: 1px; height: 160px; background: var(--divider);
  }
  .details {
    position: absolute; left: 262px; top: 84px;
    font-family: "Lato", sans-serif; color: var(--ink-light);
  }
  .person-name {
    font-weight: 900; font-size: 21px; color: var(--mint);
    text-transform: uppercase; letter-spacing: 0.3px; line-height: 1;
  }
  .person-name .degree { font-weight: 400; text-transform: none; }
  .person-role { font-size: 15px; margin-top: 4px; }
  .company {
    font-size: 14px; color: var(--mint); text-transform: uppercase;
    letter-spacing: 0.5px; margin-top: 18px;
  }
  .contact-line {
    display: flex; align-items: center; gap: 8px;
    font-size: 16px; margin-top: 5px;
  }
  .contact-line svg { width: 13px; height: 13px; flex: none; }

  /* brand side */
  .brand-lockup {
    position: absolute; inset: 0;
    display: flex; align-items: center; justify-content: center; gap: 26px;
  }
  .brand-lockup .square {
    width: 58px; height: 58px; background: var(--silver);
  }
  .brand-lockup .wordmark {
    font-family: "Source Code Pro", monospace; font-weight: 300;
    font-size: 38px; letter-spacing: 12px; color: var(--silver);
  }
</style>
</head>
<body>
<main class="sheet">
  <section class="card card--contact">
    <div class="brand-mark">Torvexa</div>
    <div class="divider"></div>
    <div class="details">
      <h1 class="person-name">Liam Brantly<span class="degree">, PhD</span></h1>
      <p class="person-role">Roboticist</p>
      <p class="company">Torvexa Consulting</p>
      <p class="contact-line">
        <svg viewBox="0 0 16 16" aria-hidden="true"><path fill="var(--mint)" d="M3 2h3l1.5 3.5-2 1.2a8 8 0 0 0 3.8 3.8l1.2-2L14 10v3a1 1 0 0 1-1 1A12 12 0 0 1 2 3a1 1 0 0 1 1-1z"/></svg>
        318.572.6094
      </p>
      <p class="contact-line">
        <svg viewBox="0 0 16 16" aria-hidden="true"><rect x="1" y="3" width="14" height="10" fill="var(--mint)"/><path d="M1.5 3.5 8 9l6.5-5.5" fill="none" stroke="var(--card)" stroke-width="1.4"/></svg>
        info@torvexamail.com
      </p>
    </div>
  </section>

  <section class="card card--brand">
    <div class="brand-lockup">
      <span class="square"></span>
      <span class="wordmark">TORVEXA</span>
    </div>
  </section>
</main>
</body>
</html>
```